Business Card Design

I used to run a Mountaineering school and am getting back into business and just want a generic type card with an adventure theme. Core activities will be mountaineering, rock climbing, canyoning, expeditions, cross country skiing,

Industry/Entity Type

School

Contact Information for Business Card

Colin Hartley Adventure Guide
email: brightfoxcolin@mailbox-example.com
+61427 836 259.

```html
<!DOCTYPE html>
<html lang="en">
<head>
<meta charset="utf-8">
<title>Ridgeway Alpine – Business Card</title>
<link rel="stylesheet" href="https://fonts.googleapis.com/css2?family=Exo+2:wght@600;700&display=swap">
<style>
  :root {
    --backdrop: #8e8e8e;
    --card-white: #ffffff;
    --brand-blue: #0c67b4;
    --name-blue: #1a5aa8;
    --brand-orange: #fbb03b;
    --snow: #ffffff;
  }
  * { margin: 0; padding: 0; box-sizing: border-box; }
  html, body {
    width: 1200px; height: 1012px; overflow: hidden;
    background: var(--backdrop);
    font-family: "Exo 2", "Arial", sans-serif;
  }
  .card {
    position: absolute; left: 100px; top: 220px;
    width: 1000px; height: 572px;
    background: var(--card-white);
    overflow: hidden;
    box-shadow: 0 14px 30px rgba(0,0,0,.35);
  }
  .card-shapes { position: absolute; inset: 0; }
  .brand {
    position: absolute; left: 56px; top: 58px;
    display: flex; align-items: center; gap: 14px;
    color: var(--brand-orange); font-weight: 700; font-size: 40px; letter-spacing: .5px;
  }
  .brand-dot { width: 22px; height: 22px; border-radius: 50%; background: var(--brand-blue); }
  .holder-name {
    position: absolute; left: 56px; top: 168px;
    color: var(--name-blue); font-weight: 700; font-size: 46px;
  }
  .contact {
    position: absolute; left: 56px; top: 280px;
    list-style: none; color: var(--brand-orange); font-weight: 600; font-size: 23px;
  }
  .contact li { display: flex; align-items: center; gap: 22px; height: 54px; }
  .contact svg { width: 44px; height: 32px; flex: none; }
  .services {
    position: absolute; right: 40px; top: 80px; width: 330px;
    list-style: none; color: var(--name-blue); font-weight: 600; font-size: 21px;
  }
  .services li {
    border-bottom: 2px solid var(--brand-orange);
    line-height: 27px; padding-right: 0;
  }
  .services li:nth-child(1) { margin-left: 150px; text-align: left; }
  .services li:nth-child(2) { margin-left: 110px; }
  .services li:nth-child(3) { margin-left: 85px; }
  .services li:nth-child(4) { margin-left: 50px; }
  .services li:nth-child(5) { margin-left: 0; }
  .mountain-art {
    position: absolute; left: 620px; top: 300px; width: 330px; height: 150px;
  }
  .role-title {
    position: absolute; right: 40px; bottom: 26px;
    color: var(--brand-orange); font-weight: 700; font-size: 29px;
  }
</style>
</head>
<body>
  <article class="card">
    <svg class="card-shapes" viewBox="0 0 1000 572" aria-hidden="true">
      <polygon points="0,250 630,250 630,395 1000,395 1000,572 0,572" fill="var(--brand-blue)"/>
      <polygon points="0,490 560,490 545,512 0,512" fill="var(--brand-orange)"/>
      <polygon points="590,490 1000,490 1000,498 585,498" fill="var(--brand-orange)"/>
      <polygon points="0,512 545,512 540,520 0,520" fill="var(--card-white)"/>
    </svg>

    <div class="brand"><span class="brand-dot"></span>Ridgeway Alpine</div>

    <h1 class="holder-name">Colin Hartley</h1>

    <ul class="contact">
      <li>
        <svg viewBox="0 0 44 32"><rect x="1" y="1" width="42" height="30" fill="var(--brand-orange)"/><polyline points="1,1 22,18 43,1" fill="none" stroke="var(--brand-blue)" stroke-width="2"/></svg>
        brightfoxcolin@mailbox-example.com
      </li>
      <li>
        <svg viewBox="0 0 44 32"><path d="M14 4c-3 0-6 3-5 8 2 8 9 15 17 17 5 1 8-2 8-5l-5-4-4 3c-4-2-7-5-9-9l3-4z" fill="var(--brand-orange)"/></svg>
        +61427 836 259
      </li>
    </ul>

    <ul class="services">
      <li>Mountaineering</li>
      <li>Rock climbing</li>
      <li>Canyoning</li>
      <li>Expeditions</li>
      <li>Cross Country Skiing</li>
    </ul>

    <div class="mountain-art" role="img" aria-label="Line illustration of snowy mountain peaks with a climber celebrating" style="background: linear-gradient(180deg, var(--brand-blue), #2f7fc4);"></div>

    <p class="role-title">Adventure Guide</p>
  </article>
</body>
</html>
```